Pediatric Dental Practice needs a postcard for direct mail advertising

We are looking for a creative and professional double-sided postcard design for a direct mail marketing campaign. Our goal is to attract new families to our pediatric dental practice by conveying a sense of warmth, modern care, and clinical excellence. The design should feel "boutique" and high-end yet remain fun and approachable for parents and children.

```html
<!DOCTYPE html>
<html lang="en">
<head>
<meta charset="utf-8">
<title>Maple Grove Pediatric Dentistry – Postcard</title>
<link href="https://fonts.googleapis.com/css2?family=Playfair+Display:wght@500;600&family=Poppins:wght@300;400;500;600&family=Kaushan+Script&display=swap" rel="stylesheet">
<style>
:root{
  --backdrop:#b3b3b3;
  --cream:#f3f6ec;
  --cream-soft:#f5f6f1;
  --green:#6a8a5e;
  --green-head:#6a8f5c;
  --green-light:#8fc48e;
  --ink:#1f1f1f;
  --body:#3a3a3a;
  --muted:#8a8a8a;
  --white:#ffffff;
  --line:#e4e8dc;
}
*{margin:0;padding:0;box-sizing:border-box}
html,body{width:889px;height:1200px;overflow:hidden}
body{background:var(--backdrop);position:relative;font-family:'Poppins',sans-serif;color:var(--body)}
.card{position:absolute;left:83px;width:729px;overflow:hidden}
.card-front{top:57px;height:520px;background:var(--cream)}
.card-back{top:632px;height:521px;background:var(--white)}
.abs{position:absolute}
.center{text-align:center}

/* front */
.hero-photo{position:absolute;left:0;top:0}
.brand-mark{width:46px;height:46px;border-radius:50%;background:var(--green-light)}
.brand-name{font-family:'Poppins',sans-serif;font-weight:500;color:var(--ink)}
.front-brand{left:84px;top:50px;width:200px;display:flex;flex-direction:column;align-items:center}
.front-brand .brand-name{font-size:15px;line-height:18px;margin-top:10px;text-align:center}
.headline{left:20px;width:328px;top:152px;font-family:'Playfair Display',serif;font-weight:500;font-size:35px;line-height:38px;text-align:center;color:var(--ink)}
.headline .accent{color:var(--green-head)}
.tagline{left:40px;width:288px;top:257px;font-size:10px;line-height:14px;font-weight:300;text-align:center;color:var(--body)}
.values{top:312px;left:24px;width:320px;display:flex;justify-content:space-between}
.value{width:106px;display:flex;flex-direction:column;align-items:center}
.value-icon{width:44px;height:44px;border-radius:50%;border:1px solid #b9c9a8;display:flex;align-items:center;justify-content:center}
.value-label{margin-top:6px;font-size:10px;line-height:14px;text-align:center;color:var(--body)}
.front-band{left:0;top:0}
.welcome{left:58px;top:430px;width:160px;font-family:'Kaushan Script',cursive;color:var(--white);font-size:22px;line-height:30px;transform:rotate(-6deg)}
.welcome .second{padding-left:14px;display:block}
.band-divider{left:228px;top:433px;width:1px;height:54px;background:rgba(255,255,255,.8)}
.cal-icon{left:254px;top:444px}
.book{left:305px;top:432px;color:var(--white)}
.book-kicker{font-size:10px;letter-spacing:.3px;font-weight:400}
.book-phone{font-size:22px;font-weight:600;line-height:28px}
.book-url{font-size:12px;font-weight:300;line-height:14px}
.badge{left:561px;top:372px;width:92px;height:92px;border-radius:50%;background:var(--cream-soft);border:2px solid var(--white);display:flex;flex-direction:column;align-items:center;justify-content:center}
.badge-dot{width:14px;height:14px;border-radius:50%;background:var(--green-light);margin-bottom:3px}
.badge-text{font-size:8px;line-height:14px;text-align:center;color:var(--body)}

/* back */
.back-divider{left:365px;top:0;width:1px;height:465px;background:var(--line)}
.back-title{left:39px;top:36px;font-family:'Playfair Display',serif;font-weight:600;font-size:20px;line-height:25px;color:var(--ink)}
.back-title .accent{color:var(--green-head);display:block}
.back-intro{left:39px;top:93px;width:285px;font-size:9.6px;line-height:14px;color:var(--body)}
.features{left:40px;top:162px;width:288px;display:flex;justify-content:space-between}
.feature{width:90px;position:relative;display:flex;flex-direction:column;align-items:center}
.feature + .feature::before{content:"";position:absolute;left:-4px;top:118px;width:1px;height:62px;background:var(--line)}
.feature-photo{width:90px;height:103px;border-radius:8px}
.feature-icon{width:34px;height:34px;border-radius:50%;background:var(--cream-soft);margin-top:-17px;display:flex;align-items:center;justify-content:center;position:relative}
.feature-title{margin-top:6px;font-size:8.6px;line-height:10.5px;font-weight:500;text-align:center;color:var(--ink)}
.feature-text{margin-top:3px;font-size:7.2px;line-height:10px;text-align:center;color:var(--body);width:100px;font-weight:300}
.doctor{left:39px;top:366px;width:289px;height:84px;border-radius:12px;background:var(--cream-soft)}
.doctor-photo{position:absolute;left:10px;top:13px;width:60px;height:60px;border-radius:50%}
.doctor-name{position:absolute;left:83px;top:8px;font-family:'Kaushan Script',cursive;color:var(--green-head);font-size:13px}
.doctor-bio{position:absolute;left:83px;top:28px;width:196px;font-size:7.3px;line-height:10px;color:var(--body);font-weight:300}
.back-brand{left:376px;top:42px;display:flex;align-items:center;gap:8px}
.back-brand .brand-mark{width:30px;height:30px}
.back-brand .brand-name{font-size:13px}
.stamp{left:623px;top:40px;width:67px;height:72px;background:var(--cream)}
.contact-strip{left:365px;top:357px;width:364px;height:14px;background:var(--cream)}
.contact-strip span{position:absolute;left:17px;top:1px;font-size:8.4px;font-weight:600;color:var(--ink)}
.contact-list{left:383px;top:376px;list-style:none}
.contact-list li{display:flex;align-items:flex-start;gap:6px;font-size:9.4px;line-height:15px;color:var(--ink)}
.contact-list svg{margin-top:3px;flex:none}
.hours-divider{left:556px;top:380px;width:1px;height:68px;background:var(--line)}
.hours{left:576px;top:377px;border-collapse:collapse}
.hours td{font-size:7.4px;line-height:14.5px;color:var(--body);padding:0}
.hours td.day{color:var(--muted);width:25px}
.back-band{left:0;top:465px;width:729px;height:56px;background:var(--green);color:var(--white);text-align:center}
.back-band .lead{font-weight:600;font-size:11.5px;padding-top:11px;line-height:15px}
.back-band .towns{font-weight:300;font-size:11.5px;line-height:15px}
</style>
</head>
<body>

<section class="card card-front">
  <svg class="hero-photo" width="729" height="520" viewBox="0 0 729 520" role="img" aria-label="Photo of a smiling girl in a teal dental chair with a masked dentist beside her in a bright clinic">
    <defs>
      <linearGradient id="photoTone" x1="0" y1="0" x2="1" y2="1">
        <stop offset="0" stop-color="#e8ddcf"/>
        <stop offset=".45" stop-color="#c8b29a"/>
        <stop offset=".7" stop-color="#4fa3b5"/>
        <stop offset="1" stop-color="#e9ecef"/>
      </linearGradient>
    </defs>
    <path d="M320 0 H729 V470 H390 C385 330 430 150 320 0 Z" fill="url(#photoTone)"/>
  </svg>

  <svg class="front-band abs" width="729" height="520" viewBox="0 0 729 520" aria-hidden="true">
    <path d="M0 425 C120 395 250 420 380 418 C500 416 600 385 729 418 V520 H0 Z" fill="var(--green)"/>
  </svg>

  <div class="front-brand abs">
    <div class="brand-mark"></div>
    <div class="brand-name">Maple Grove<br>Pediatric Dentistry</div>
  </div>

  <h1 class="headline abs">Healthy smiles.<br><span class="accent">Happy childhoods.</span></h1>
  <p class="tagline abs">Pediatric dental care that feels good and makes a lasting impact.</p>

  <div class="values abs">
    <div class="value">
      <div class="value-icon">
        <svg width="24" height="22" viewBox="0 0 24 22" fill="none" stroke="var(--green)" stroke-width="1.3"><path d="M12 20 C4 14 1 10 2 6 C3 2 8 1 12 5 C16 1 21 2 22 6 C23 10 20 14 12 20 Z"/></svg>
      </div>
      <div class="value-label">Compassionate<br>Care</div>
    </div>
    <div class="value">
      <div class="value-icon">
        <svg width="24" height="24" viewBox="0 0 24 24" fill="none" stroke="var(--green)" stroke-width="1.3"><path d="M12 22 V11"/><path d="M12 12 C6 12 3 8 4 4 C8 4 12 7 12 12 Z"/><path d="M12 12 C18 12 21 8 20 4 C16 4 12 7 12 12 Z"/></svg>
      </div>
      <div class="value-label">Comforting<br>Environment</div>
    </div>
    <div class="value">
      <div class="value-icon">
        <svg width="22" height="24" viewBox="0 0 22 24" fill="none" stroke="var(--green)" stroke-width="1.3"><path d="M6 2 C2 2 1 6 2 10 C3 13 4 15 5 22 C6 23 7 22 8 18 C9 15 10 15 11 15 C12 15 13 15 14 18 C15 22 16 23 17 22 C18 15 19 13 20 10 C21 6 20 2 16 2 C14 2 13 3 11 3 C9 3 8 2 6 2 Z"/></svg>
      </div>
      <div class="value-label">Built For<br>Little Smiles</div>
    </div>
  </div>

  <p class="welcome abs">Now welcoming<span class="second">new families!</span></p>
  <div class="band-divider abs"></div>
  <svg class="cal-icon abs" width="34" height="32" viewBox="0 0 34 32" fill="none" stroke="#fff" stroke-width="1.6">
    <rect x="1" y="4" width="28" height="26" rx="3"/><path d="M1 11 H29 M8 1 V7 M22 1 V7"/>
    <path d="M6 16 H9 M12 16 H15 M6 21 H9 M6 26 H9"/>
    <circle cx="24" cy="23" r="7" fill="var(--green)"/><path d="M24 19 V23 L27 25"/>
  </svg>
  <div class="book abs">
    <div class="book-kicker">BOOK YOUR VISIT TODAY</div>
    <div class="book-phone">(555) 014-2600</div>
    <div class="book-url">maplegrovekids.com</div>
  </div>

  <div class="badge abs">
    <div class="badge-dot"></div>
    <div class="badge-text">A Positive<br>Dental Experience<br>for Little Smiles<br>That Last</div>
  </div>
</section>

<section class="card card-back">
  <div class="back-divider abs"></div>

  <h2 class="back-title abs">Growing Confident Smiles<span class="accent">Every Step of the Way</span></h2>
  <p class="back-intro abs">At Maple Grove Pediatric Dentistry, we create a warm, welcoming space where kids feel at ease and parents feel confident. Our goal is to build healthy habits, bright smiles, and lifelong trust.</p>

  <div class="features abs">
    <div class="feature">
      <div class="feature-photo" role="img" aria-label="Photo of a colorful kids play corner with toys and wall decals" style="background:linear-gradient(160deg,#dfe6c8,#c9b48a 70%,#b7a27a)"></div>
      <div class="feature-icon">
        <svg width="16" height="16" viewBox="0 0 16 16" fill="none" stroke="var(--green)" stroke-width="1.1"><circle cx="8" cy="8" r="7"/><circle cx="5.5" cy="6.5" r=".5" fill="var(--green)"/><circle cx="10.5" cy="6.5" r=".5" fill="var(--green)"/><path d="M5 10 C6.5 12 9.5 12 11 10"/></svg>
      </div>
      <div class="feature-title">Kid-Friendly<br>Amenities</div>
      <div class="feature-text">Thoughtful comforts designed for kids and parents.</div>
    </div>
    <div class="feature">
      <div class="feature-photo" role="img" aria-label="Photo of a modern treatment room with a teal dental chair" style="background:linear-gradient(170deg,#e6ebe0,#c9d2c3 50%,#4f98a8 80%,#c98f5c)"></div>
      <div class="feature-icon">
        <svg width="12" height="16" viewBox="0 0 12 16" fill="none" stroke="var(--green)" stroke-width="1.1"><rect x="1" y="1" width="10" height="14" rx="1.5"/><path d="M4 5 C4 4 5 4 6 4.5 C7 4 8 4 8 5 C8 7 7 8 7 9 L6 8 L5 9 C5 8 4 7 4 5 Z"/><circle cx="6" cy="12.5" r=".6"/></svg>
      </div>
      <div class="feature-title">Modern<br>Technology</div>
      <div class="feature-text">Advanced tools for gentle, efficient, and accurate care.</div>
    </div>
    <div class="feature">
      <div class="feature-photo" role="img" aria-label="Photo of a dentist showing a plush dinosaur to a group of young children" style="background:linear-gradient(160deg,#c9b59a,#4f9aa5 45%,#5aa05a 70%,#d8c6b0)"></div>
      <div class="feature-icon">
        <svg width="18" height="16" viewBox="0 0 18 16" fill="none" stroke="var(--green)" stroke-width="1.1"><path d="M9 13 C5 10 4 8 4.5 6 C5 4 7.5 4 9 6 C10.5 4 13 4 13.5 6 C14 8 13 10 9 13 Z"/><path d="M1 6 C1 10 4 13 7 15 M17 6 C17 10 14 13 11 15"/></svg>
      </div>
      <div class="feature-title">Compassionate<br>Expertise</div>
      <div class="feature-text">Pediatric dental specialist focused on your child's well-being.</div>
    </div>
  </div>

  <div class="doctor abs">
    <div class="doctor-photo" role="img" aria-label="Portrait photo of the pediatric dentist" style="background:radial-gradient(circle at 50% 40%,#e2c8b2,#9fb2b9 70%,#8aa0a8)"></div>
    <div class="doctor-name">Meet Dr. Lindell</div>
    <p class="doctor-bio">A board-certified pediatric dentist and dad of two who believes every child deserves a positive dental experience that sets the foundation for a lifetime of healthy smiles.</p>
  </div>

  <div class="back-brand abs">
    <div class="brand-mark"></div>
    <div class="brand-name">Maple Grove Pediatric Dentistry</div>
  </div>
  <div class="stamp abs"></div>

  <div class="contact-strip abs"><span>CONTACT US TO BOOK YOUR VISIT TODAY</span></div>
  <ul class="contact-list abs">
    <li><svg width="9" height="9" viewBox="0 0 10 10"><circle cx="5" cy="5" r="5" fill="#dfe8d6"/><path d="M3.3 2.6 L4.2 2.4 L4.7 3.8 L4.1 4.3 C4.4 5 5 5.6 5.7 5.9 L6.2 5.3 L7.6 5.8 L7.4 6.7 C5 7 3 5 3.3 2.6 Z" fill="var(--green)"/></svg>(555) 014-2600</li>
    <li><svg width="9" height="9" viewBox="0 0 10 10"><circle cx="5" cy="5" r="5" fill="#dfe8d6"/><rect x="2.6" y="4" width="4.8" height="2.6" rx=".5" fill="var(--green)"/><rect x="3.5" y="2.6" width="3" height="1.2" fill="var(--green)"/></svg>(555) 014-2610</li>
    <li><svg width="9" height="9" viewBox="0 0 10 10"><circle cx="5" cy="5" r="5" fill="#dfe8d6"/><rect x="2.5" y="3.3" width="5" height="3.4" rx=".5" fill="var(--green)"/><path d="M2.7 3.5 L5 5.2 L7.3 3.5" stroke="#dfe8d6" stroke-width=".6" fill="none"/></svg>hello@maplegrovekids.com</li>
    <li><svg width="9" height="9" viewBox="0 0 10 10"><circle cx="5" cy="5" r="5" fill="#dfe8d6"/><path d="M5 8 C3.5 6 3 5 3 4.2 A2 2 0 0 1 7 4.2 C7 5 6.5 6 5 8 Z" fill="var(--green)"/><circle cx="5" cy="4.2" r=".7" fill="#dfe8d6"/></svg><span style="line-height:11px;padding-top:2px">48 Orchard Lane, Suite 210,<br>Fairview, CT 06000</span></li>
  </ul>
  <div class="hours-divider abs"></div>
  <table class="hours abs">
    <tr><td class="day">Mon</td><td>8:30am - 4:30pm</td></tr>
    <tr><td class="day">Tues</td><td>8:30am - 4:30pm</td></tr>
    <tr><td class="day">Wed</td><td>Closed</td></tr>
    <tr><td class="day">Thurs</td><td>8:30am - 4:30pm</td></tr>
    <tr><td class="day">Fri</td><td>8:30am - 4:30pm</td></tr>
  </table>

  <div class="back-band abs">
    <div class="lead">Proudly serving families in</div>
    <div class="towns">Fairview • Brookside • Millbrook • Ashford Hills • Cedar Point and surrounding communities in Connecticut</div>
  </div>
</section>

</body>
</html>
```